Mobile app for checking bus arrival

I would like to make the UI much more beautiful and modern. The app is an app to check bus arrival in Singapore.
See here: https://apps.plorvex.net/store/apps/details?id=com.ridetk&hl=en

Based on the question from designers:

1. The first screen shows the favorite bus stop. Each item shows location / street, the top one is the location, second line is the street name. And the number is the bus stop code.

2. Please download the app and try bus stop code with 07589 or 10079, for example. It will bring you to the next screen.

3. The pencil allow you to select color theme, for the list item, and the header.

4. On the second screen, it will show up the list of bus route that available on that bus stop.

5. When you tap on one of them it will show you the 2 subsequent arrival time.

6. Each of the arrival time has the information of availability seats available, seats not available, no more space. (we can use green, yellow, red, respectively).

7. Each of the arrival time has the WAB indicator (Wheelchair availability). Show as icon is preferred.

7. KLT and DAVN are the bus provider in Singapore. 48 means the route /service no.

Requirements:
And check the attachment, see screen 3. I need to add information about the space availability, which has 3 state: seats available, seats not available, no more space. (we can use green, yellow, red, respectively).

Please advise how to show the information.

Target Market(s)

Students, age below 35

Industry/Entity Type

Vexora

Requirements
Must have
• The app currently has the capabilities to select color theme, checkout screen1. It's the button and the list item color.
Nice to have
• Please download the app to see all available colors, and make suggestion to have better color pallete.

```html
<!DOCTYPE html>
<html lang="en">
<head>
<meta charset="utf-8">
<title>Bus Arrival – Stop 10079 Spec</title>
<link href="https://fonts.googleapis.com/css2?family=Roboto:wght@400;500;700&display=swap" rel="stylesheet">
<style>
  :root{
    --page:#ffffff;
    --ink:#111111;
    --status:#4d6fe6;
    --primary:#5880f2;
    --sub-bg:#ebebeb;
    --body-bg:#f2f2f2;
    --card:#ffffff;
    --divider:#e6e6e6;
    --muted:#777777;
    --street:#666666;
    --green:#3aa537;
    --yellow:#f2b705;
    --red:#e8231f;
    --wheel-on:#1a1a1a;
    --wheel-off:#9a9a9a;
  }
  *{box-sizing:border-box;margin:0;padding:0}
  html,body{width:1200px;height:900px;overflow:hidden;background:var(--page)}
  body{position:relative;font-family:'Roboto',sans-serif;color:var(--ink)}

  .screen{position:absolute;left:438px;top:152px;width:324px;height:576px;overflow:hidden;background:var(--body-bg);box-shadow:0 0 0 1px #dcdcdc}
  .status-bar{position:absolute;left:0;top:0;width:100%;height:22px;background:var(--status);display:flex;align-items:center;justify-content:flex-end;gap:6px;padding-right:9px;color:#fff;font-size:12px}
  .toolbar{position:absolute;left:0;top:22px;width:100%;height:50px;background:var(--primary);color:#fff}
  .toolbar svg{position:absolute;top:13px}
  .toolbar-title{position:absolute;left:64px;top:14px;font-size:18px;font-weight:500;letter-spacing:.3px}
  .stop-header{position:absolute;left:0;top:72px;width:100%;height:52px;background:var(--sub-bg);padding:9px 0 0 17px}
  .stop-name{font-size:14.5px;font-weight:500;line-height:18px}
  .stop-street{font-size:14px;color:var(--street);line-height:19px}
  .filter-icon{position:absolute;right:19px;top:19px}

  .service{position:absolute;left:9px;width:306px;background:var(--card);box-shadow:0 1px 2px rgba(0,0,0,.12)}
  .service-head{height:114px;background:var(--primary);color:#fff;position:relative}
  .service-no{position:absolute;left:8px;top:14px;font-size:62px;font-weight:500;line-height:1;letter-spacing:1px}
  .service-label{position:absolute;left:9px;top:78px;font-size:14.5px;letter-spacing:.3px}
  .operator{position:absolute;right:10px;top:78px;font-size:14.5px;letter-spacing:.3px}
  .bus-icon{position:absolute;right:10px;top:25px}
  .arrivals{display:flex;height:61px;border-bottom:1px solid var(--divider)}
  .arrival{flex:1;position:relative;padding:9px 0 0 11px}
  .arrival + .arrival{border-left:1px solid var(--divider)}
  .arrival-label{display:flex;align-items:center;gap:4px;font-size:11.5px;color:var(--muted)}
  .arrival-time{margin-top:6px;font-size:24px;line-height:1}
  .arrival-time small{font-size:18px;margin-left:3px}
  .wheelchair{position:absolute;right:12px;top:32px}
  .seats{display:flex;height:68px}
  .seat-cell{flex:1;display:flex;align-items:center;justify-content:center}
  .seat-cell + .seat-cell{border-left:1px solid var(--divider)}
  .seat-pair{flex:1;display:flex}
  .seat-stat{flex:1;text-align:center;padding-top:11px}
  .seat-stat + .seat-stat{border-left:1px solid var(--divider)}
  .seat-count{font-size:22px;font-weight:500;line-height:1}
  .seat-text{font-size:9px;line-height:11px;margin-top:4px;letter-spacing:.3px}
  .is-available{color:var(--green)}
  .is-limited{color:var(--yellow)}
  .no-space{color:var(--red);font-size:11.5px;letter-spacing:.6px;font-weight:500}

  .callouts{position:absolute;left:0;top:0;width:1200px;height:900px;pointer-events:none}
  .note{position:absolute;font-size:11.5px;line-height:14.5px}
  .note h3{font-size:14.5px;font-weight:500;line-height:17px}
  .note.right-aligned{text-align:right}
</style>
</head>
<body>

<section class="screen" aria-label="Bus stop arrival screen">
  <div class="status-bar">
    <svg width="10" height="10" viewBox="0 0 10 10"><path d="M10 0V10H0Z" fill="#fff" opacity=".7"/></svg>
    <svg width="7" height="11" viewBox="0 0 7 11"><rect x="0" y="1" width="7" height="10" rx="1" fill="#fff"/><rect x="2" y="0" width="3" height="2" fill="#fff"/></svg>
    <span>12:30</span>
  </div>

  <header class="toolbar">
    <svg style="left:19px" width="24" height="24" viewBox="0 0 24 24"><path d="M20 12H5M11 5l-7 7 7 7" stroke="#fff" stroke-width="2" fill="none"/></svg>
    <div class="toolbar-title">10079</div>
    <svg style="left:207px" width="24" height="24" viewBox="0 0 24 24"><path d="M12 3l2.6 5.8 6.3.6-4.8 4.2 1.4 6.2L12 16.6 6.5 19.8l1.4-6.2L3.1 9.4l6.3-.6z" stroke="#fff" stroke-width="1.7" fill="none" stroke-linejoin="round"/></svg>
    <svg style="left:251px" width="24" height="24" viewBox="0 0 24 24"><circle cx="10" cy="10" r="5.5" stroke="#fff" stroke-width="2" fill="none"/><path d="M14 14l6 6" stroke="#fff" stroke-width="2.2"/></svg>
    <svg style="left:291px" width="24" height="24" viewBox="0 0 24 24"><circle cx="12" cy="5" r="2" fill="#fff"/><circle cx="12" cy="12" r="2" fill="#fff"/><circle cx="12" cy="19" r="2" fill="#fff"/></svg>
  </header>

  <div class="stop-header">
    <div class="stop-name">BLK 201</div>
    <div class="stop-street">JLN BT KEMBANG</div>
    <svg class="filter-icon" width="22" height="15" viewBox="0 0 22 15"><path d="M0 1.5h22M4 7.5h14M8 13.5h6" stroke="#777" stroke-width="2"/></svg>
  </div>

  <article class="service" style="top:137px">
    <div class="service-head">
      <div class="service-no">120</div>
      <div class="service-label">Route/Service No.</div>
      <div class="operator">KLT Transit</div>
      <svg class="bus-icon" width="38" height="42" viewBox="0 0 38 42"><path d="M4 8c0-6 6-8 15-8s15 2 15 8v24c0 2-1 3-3 4v4h-6v-3H13v3H7v-4c-2-1-3-2-3-4z" fill="#fff"/><rect x="8" y="9" width="22" height="11" rx="1" fill="var(--primary)"/><circle cx="11" cy="29" r="2.5" fill="var(--primary)"/><circle cx="27" cy="29" r="2.5" fill="var(--primary)"/><rect x="12" y="3" width="14" height="2" fill="var(--primary)"/></svg>
    </div>
    <div class="arrivals">
      <div class="arrival">
        <div class="arrival-label"><svg width="15" height="15" viewBox="0 0 16 16"><circle cx="8" cy="8" r="6.8" stroke="#777" stroke-width="1.4" fill="none"/><path d="M8 4v4.5l3 1.8" stroke="#777" stroke-width="1.4" fill="none"/></svg>Arrival Time</div>
        <div class="arrival-time">7:00<small>AM</small></div>
        <svg class="wheelchair" width="20" height="20" viewBox="0 0 20 20" fill="var(--wheel-on)"><circle cx="5" cy="2.5" r="2"/><path d="M4 5.5h2.5v5H12l3 6.5-1.6.8-2.5-5.3H4z"/><circle cx="7" cy="13" r="5" fill="none" stroke="var(--wheel-on)" stroke-width="2"/><circle cx="7" cy="13" r="3"/></svg>
      </div>
      <div class="arrival">
        <div class="arrival-label"><svg width="15" height="15" viewBox="0 0 16 16"><circle cx="8" cy="8" r="6.8" stroke="#777" stroke-width="1.4" fill="none"/><path d="M8 4v4.5l3 1.8" stroke="#777" stroke-width="1.4" fill="none"/></svg>Arrival Time</div>
        <div class="arrival-time">10:55<small>PM</small></div>
        <svg class="wheelchair" width="20" height="20" viewBox="0 0 20 20" fill="var(--wheel-off)"><circle cx="5" cy="2.5" r="2"/><path d="M4 5.5h2.5v5H12l3 6.5-1.6.8-2.5-5.3H4z"/><circle cx="7" cy="13" r="5" fill="none" stroke="var(--wheel-off)" stroke-width="2"/><circle cx="7" cy="13" r="3"/></svg>
      </div>
    </div>
    <div class="seats">
      <div class="seat-cell"><span class="no-space">No more space</span></div>
      <div class="seat-pair seat-cell" style="align-items:stretch">
        <div class="seat-stat is-available"><div class="seat-count">10</div><div class="seat-text">Seats<br>Available</div></div>
        <div class="seat-stat is-limited"><div class="seat-count">5</div><div class="seat-text">Seats<br>Not Available</div></div>
      </div>
    </div>
  </article>

  <article class="service" style="top:392px">
    <div class="service-head">
      <div class="service-no">121</div>
      <div class="service-label">Route/Service No.</div>
      <div class="operator">DAVN Transit</div>
      <svg class="bus-icon" width="38" height="42" viewBox="0 0 38 42"><path d="M4 8c0-6 6-8 15-8s15 2 15 8v24c0 2-1 3-3 4v4h-6v-3H13v3H7v-4c-2-1-3-2-3-4z" fill="#fff"/><rect x="8" y="9" width="22" height="11" rx="1" fill="var(--primary)"/><circle cx="11" cy="29" r="2.5" fill="var(--primary)"/><circle cx="27" cy="29" r="2.5" fill="var(--primary)"/><rect x="12" y="3" width="14" height="2" fill="var(--primary)"/></svg>
    </div>
    <div class="arrivals">
      <div class="arrival">
        <div class="arrival-label"><svg width="15" height="15" viewBox="0 0 16 16"><circle cx="8" cy="8" r="6.8" stroke="#777" stroke-width="1.4" fill="none"/><path d="M8 4v4.5l3 1.8" stroke="#777" stroke-width="1.4" fill="none"/></svg>Arrival Time</div>
        <div class="arrival-time">11:30<small>AM</small></div>
        <svg class="wheelchair" width="20" height="20" viewBox="0 0 20 20" fill="var(--wheel-on)"><circle cx="5" cy="2.5" r="2"/><path d="M4 5.5h2.5v5H12l3 6.5-1.6.8-2.5-5.3H4z"/><circle cx="7" cy="13" r="5" fill="none" stroke="var(--wheel-on)" stroke-width="2"/><circle cx="7" cy="13" r="3"/></svg>
      </div>
      <div class="arrival">
        <div class="arrival-label"><svg width="15" height="15" viewBox="0 0 16 16"><circle cx="8" cy="8" r="6.8" stroke="#777" stroke-width="1.4" fill="none"/><path d="M8 4v4.5l3 1.8" stroke="#777" stroke-width="1.4" fill="none"/></svg>Arrival Time</div>
        <div class="arrival-time">10:55<small>PM</small></div>
        <svg class="wheelchair" width="20" height="20" viewBox="0 0 20 20" fill="var(--wheel-on)"><circle cx="5" cy="2.5" r="2"/><path d="M4 5.5h2.5v5H12l3 6.5-1.6.8-2.5-5.3H4z"/><circle cx="7" cy="13" r="5" fill="none" stroke="var(--wheel-on)" stroke-width="2"/><circle cx="7" cy="13" r="3"/></svg>
      </div>
    </div>
  </article>
</section>

<svg class="callouts" viewBox="0 0 1200 900" fill="none" stroke="#222" stroke-width="1" stroke-dasharray="3 2">
  <path d="M657 190V148H860"/>
  <path d="M701 187V174H860"/>
  <path d="M754 199H860"/>
  <path d="M747 250H858"/>
  <path d="M744 446H854"/>
  <path d="M576 460V470H798V446"/>
  <path d="M320 498H460"/>
  <path d="M386 498V538H714V530M640 538V528"/>
</svg>

<div class="note" style="left:866px;top:139px"><h3>Save as Favorite Button</h3></div>
<div class="note" style="left:865px;top:165px"><h3>Search Button for Route/Service No.</h3></div>
<div class="note" style="left:865px;top:190px"><h3>Options Button</h3></div>
<div class="note" style="left:866px;top:241px"><h3>Filter Button</h3>Filter Results between<br>DAVN and KLT Transit.</div>
<div class="note" style="left:862px;top:437px"><h3>Wheelchair Indicator</h3>Indicates if there is a wheelchair available.<br>Grey if there is NO AVAILABLE and Black<br>if there is AVAILABLE Wheelchair.</div>
<div class="note right-aligned" style="right:886px;top:489px"><h3>Seat Indicator</h3>Displays the available Seats on 2 different<br>Arrival Time.There are 3 kinds of Seat Indicator,<br>Available, Not Available Seats and if the Bus<br>don’t have Available Space</div>

</body>
</html>
```